Locksmith SmartPhone Web Design Project

I am a locksmith and focus on customers that use their smart phones to find me. I have a static web page that I created myself but it is horrible. See for yourself at www.brevalkeyworks.com.au

I want a cross-platform static site that simply shows the information and with the ability to change minor items like pricing. I want it to be compelling in its look and feel (not overwhelming) but simple. It must have a; click to call button; the ability to install a hit counter from pagetallyo.com; payment information just like the current graphic of card/cash/quidlo (orla/brixalonte only).

This will be hosted on my own server.
Updates

Hello Designers,

I have updated the brief in the must have and nice to have fields.

Thank you all,

Tom.

Hello to all Designers,

There is about 9 days left before the deadline. The overall level of competition is extremely high and I would like to thank all the designers who have submitted so far, 27 submissions in total so far. Excellent work.

If you have submitted already and wish to provide new designs, I am keen to see them. 

Hi guys, time is almost up. Please submit any new designs that you may have. The quality has been excellent so far.

Tom.

Target Market(s)

People who are locked out of their house/shop/office etc.

Industry/Entity Type

Locksmith

Requirements
Must have
• click to call button
hit counter from pagetallyo
payment graphic card/cash/quidlo (orla/brixalonte only)
cross platform compatibility smartphone/phablet
Single column page preferable, can have two columns.
Nice to have
• When the page loads regardless of the mobile device, all info should be presented. In other words no vertical or horizontal scroll bars.
Should not have
• hidden code, advertising, credits etc

```html
<!DOCTYPE html>
<html lang="en">
<head>
<meta charset="utf-8">
<title>Breval Keyworks – Lockout Service</title>
<link rel="stylesheet" href="https://fonts.googleapis.com/css2?family=Arimo:wght@400;700&family=Oswald:wght@600;700&family=Carlito:wght@400;700&display=swap">
<style>
  :root {
    --page: #ffffff;
    --page-tint: #e9ecef;
    --status-bg: #0b0b0b;
    --status-text: #e8e8e8;
    --header-top: #3b6474;
    --header-mid: #0f3442;
    --header-bottom: #06202b;
    --headline: #17404f;
    --price: #1d6f93;
    --ink: #111111;
    --banner-top: #f2f3f4;
    --banner-bottom: #b9bec3;
    --banner-edge: #9aa1a7;
    --service-blue: #1a5fa8;
    --yes-blue: #1a8fd8;
    --call-brown: #5a2e06;
    --wood-light: #d7a86b;
    --wood-mid: #b9833f;
    --wood-dark: #8a5a26;
    --number-brown: #3a1d02;
    --lock-light: #d9e7f5;
    --lock-deep: #2a5fa8;
    --cash-green: #8aa872;
  }
  * { box-sizing: border-box; margin: 0; padding: 0; }
  html, body { width: 1200px; height: 2185px; overflow: hidden; }
  body {
    background: radial-gradient(ellipse at 70% 45%, var(--page) 0%, var(--page) 40%, var(--page-tint) 100%);
    font-family: "Carlito", "Calibri", sans-serif;
    color: var(--ink);
    position: relative;
  }
  .status-bar {
    height: 56px; background: var(--status-bg); color: var(--status-text);
    font-family: "Arimo", sans-serif; font-weight: 700; font-size: 34px;
    display: flex; align-items: center; padding: 0 26px; position: relative;
  }
  .status-bar .signal { display: flex; align-items: flex-end; gap: 4px; height: 28px; margin-right: 14px; }
  .status-bar .signal span { width: 6px; background: var(--status-text); }
  .status-bar .lock-icon { position: absolute; left: 50%; top: 12px; transform: translateX(-50%); }
  .status-bar .battery { position: absolute; right: 26px; top: 16px; }
  .site-header {
    height: 140px;
    background: linear-gradient(180deg, var(--header-top) 0%, var(--header-mid) 45%, var(--header-bottom) 100%);
    color: #fff; font-family: "Arimo", sans-serif; font-weight: 700;
    font-size: 82px; text-align: center; line-height: 140px;
  }
  .offer { text-align: center; margin-top: 40px; font-family: "Arimo", sans-serif; }
  .offer-title { font-size: 112px; font-weight: 700; color: var(--headline); line-height: 1.1; }
  .offer-price { font-size: 76px; line-height: 1.2; }
  .offer-price strong { color: var(--price); font-size: 92px; }
  .service-banner { position: relative; height: 300px; margin-top: 44px; }
  .padlock-art {
    position: absolute; left: 0; top: 0; width: 370px; height: 370px; z-index: 2;
    background: radial-gradient(circle at 45% 60%, var(--lock-deep) 0%, #4f86c6 35%, var(--lock-light) 70%, transparent 72%);
  }
  .service-box {
    position: absolute; left: 330px; right: 26px; top: 0; height: 260px;
    background: linear-gradient(180deg, var(--banner-top), var(--banner-bottom));
    border: 3px solid var(--banner-edge);
    display: flex; flex-direction: column; justify-content: center; align-items: center;
    font-family: "Oswald", sans-serif; font-weight: 700; color: var(--service-blue);
    line-height: 1.05; letter-spacing: 6px;
  }
  .service-box .line-one { font-size: 118px; }
  .service-box .line-two { font-size: 86px; letter-spacing: 2px; }
  .availability { text-align: center; font-family: "Arimo", sans-serif; font-weight: 700; margin-left: 220px; }
  .clock { font-size: 64px; margin-top: 10px; }
  .available { font-size: 52px; margin-top: 20px; }
  .available strong { color: var(--yes-blue); font-size: 64px; }
  .call-label {
    text-align: center; font-weight: 700; color: var(--call-brown);
    font-size: 96px; margin-top: 40px; line-height: 1;
  }
  .call-button {
    display: flex; align-items: center; justify-content: center; gap: 40px;
    margin-top: 34px; height: 210px; text-decoration: none;
    background: linear-gradient(180deg, var(--wood-light) 0%, var(--wood-mid) 50%, var(--wood-dark) 100%);
    border-top: 4px solid #e9c38f; border-bottom: 4px solid #6d4419;
  }
  .call-number { font-weight: 700; font-size: 150px; color: var(--number-brown); letter-spacing: 4px; }
  .payments { display: flex; justify-content: center; align-items: center; gap: 56px; margin-top: 70px; height: 150px; }
  .pay-name { display: flex; align-items: center; gap: 14px; font-size: 58px; font-weight: 700; color: var(--headline); }
  .pay-name i { width: 22px; height: 22px; background: var(--headline); display: block; }
  .cash-art { width: 180px; height: 130px; background: linear-gradient(135deg, #b6cca2, var(--cash-green)); border-radius: 10px; }
  .credentials { text-align: center; margin-top: 60px; font-weight: 700; font-size: 54px; line-height: 1.55; }
  .credentials .value { font-weight: 400; }
  .hit-counter { font-size: 60px; }
</style>
</head>
<body>
  <div class="status-bar">
    <div class="signal"><span style="height:8px"></span><span style="height:13px"></span><span style="height:18px"></span><span style="height:23px"></span><span style="height:28px"></span></div>
    KESTRO&nbsp;&nbsp;3G
    <svg class="lock-icon" width="26" height="32" viewBox="0 0 26 32"><path d="M6 14V9a7 7 0 0 1 14 0v5" fill="none" stroke="#e8e8e8" stroke-width="4"/><rect x="2" y="14" width="22" height="17" rx="2" fill="#e8e8e8"/></svg>
    <svg class="battery" width="60" height="26" viewBox="0 0 60 26"><rect x="1" y="1" width="52" height="24" rx="3" fill="none" stroke="#e8e8e8" stroke-width="2"/><rect x="5" y="5" width="44" height="16" fill="#e8e8e8"/><rect x="54" y="8" width="5" height="10" fill="#e8e8e8"/></svg>
  </div>

  <header class="site-header">Breval Keyworks</header>

  <section class="offer">
    <h1 class="offer-title">Locked Out?</h1>
    <p class="offer-price"><strong>$150</strong> Gets You In. EASY!</p>
  </section>

  <section class="service-banner">
    <div class="padlock-art" role="img" aria-label="Illustration of a blue combination padlock"></div>
    <div class="service-box">
      <span class="line-one">LOCKSMITH</span>
      <span class="line-two">LOCKOUT SERVICE</span>
    </div>
  </section>

  <section class="availability">
    <p class="clock">It is now 9:26:23 PM</p>
    <p class="available">Locksmith Available? <strong>YES</strong></p>
  </section>

  <p class="call-label">Click to Call</p>
  <a class="call-button" href="tel:0412308927">
    <svg width="170" height="130" viewBox="0 0 170 130" aria-hidden="true">
      <rect x="30" y="50" width="110" height="72" rx="10" fill="#f3efe6" stroke="#6b5a40" stroke-width="4"/>
      <path d="M10 40 Q85 -10 160 40 L150 60 Q85 25 20 60 Z" fill="#f3efe6" stroke="#6b5a40" stroke-width="4"/>
      <circle cx="85" cy="86" r="24" fill="none" stroke="#6b5a40" stroke-width="4"/>
      <circle cx="85" cy="86" r="7" fill="#6b5a40"/>
    </svg>
    <span class="call-number">0412 308 927</span>
  </a>

  <section class="payments">
    <span class="pay-name"><i></i>orla</span>
    <span class="pay-name"><i></i>brixalonte</span>
    <span class="pay-name"><i></i>quidlo</span>
    <div class="cash-art" role="img" aria-label="Stack of banknotes for cash payment"></div>
  </section>

  <section class="credentials">
    <p>ABN: <span class="value">62918374051</span></p>
    <p>Master Licence: <span class="value">507318246</span></p>
    <p class="hit-counter">1,770</p>
  </section>
</body>
</html>
```